Tri-Fold Brochure for Awesome School App Required!

Tulvora is a unique school app that connects teachers and parents. It is about to be launched in Australia with plans for world domination soon after :)

As part of the marketing strategy, we require a professional brochure to mail out.

We want a tri-fold brochure using the Tulvora logo colours (images attached). Front and back page should be the Tulvora blue and the inside can be white with blue borders and logo or blue with white writing although we're leaving the creativity part up to you, the experts.

As an idea, attached is an example of the content and layout required (NOTE - IT REFERS TO 'PAGES' IN THE DOCUMENT BUT I DO MEAN PANELS)
Updates

Hi All,

Thanks for taking interest in designing a brochure for Tulvora. The designs so far are great.

Note - I have attached an updated Draft design document - some of the wording has changed to make it not look so 'busy'. So please take a look at the new document.

Regards

Glen

Hi All,

Thanks for your designs so far - please keep them coming.

I have attached a 'mock screens.zip' folder - it has some images for the app. Please incorporate these into new submissions.

Regards

Glen

Hi all. Just reiterating - I would like to see some of your designs with the app screen images incorporated (in the 'mock_up.zip' folder in the attachments).

Feel free to place them anywhere you see fit - they don't just have to be on the 'app screen' page as per my original brief.

Glen

Target Market(s)

Target market is school Principals and school IT decision makers.

Industry/Entity Type

Marketing

Requirements
Must have
• - Make good use of the 6 panels of the brochure but the front panel should just be the company logo (either the elongated image across the whole panel or the vertical image in the middle - whatever looks best).
- Back panel to be logo and contact details.
- Preference is for the colour scheme to remain within the Tulvora logo colours but if you think you've got a better idea, please submit it.
**PLEASE SEE THE ATTACHED SAMPLE LAYOUT DOCUMENT**
Nice to have
• Feel free to put in non-copyrighted images relating to schools.
Feel free to invert colours, but try and stick to the Tulvora colour scheme wherever possible.

```html
<!DOCTYPE html>
<html lang="en">
<head>
<meta charset="utf-8">
<title>Tulvora Tri-Fold Brochure</title>
<link rel="stylesheet" href="https://fonts.googleapis.com/css2?family=Fira+Sans+Extra+Condensed:wght@700;800;900&family=Open+Sans:wght@300;400;600;700&display=swap">
<style>
:root{
  --mint:#9dd3aa;
  --blue:#3356b8;
  --blue-light:#5a7ccf;
  --ink:#111;
  --white:#fff;
  --text:#222;
}
*{margin:0;padding:0;box-sizing:border-box}
html,body{width:900px;height:1200px;overflow:hidden}
body{background:var(--mint);position:relative;font-family:"Open Sans",sans-serif}
.sheet{position:absolute;left:63px;width:774px;height:517px;display:flex;outline:2px solid var(--white)}
.sheet--outer{top:50px}
.sheet--inner{top:633px}
.panel{position:relative;width:258px;height:100%;border-right:2px solid var(--white)}
.panel:last-child{border-right:none}
.panel--blue{background:var(--blue);color:var(--white)}
.panel--white{background:var(--white);color:var(--text)}
.app-screen{position:absolute;inset:0;background:linear-gradient(180deg,#111 0,#1a1a1a 60%,#000 100%)}
.brand{display:flex;align-items:center;gap:8px;font-family:"Open Sans",sans-serif;font-weight:300;color:var(--white)}
.brand__dot{width:26px;height:26px;border-radius:50%;background:var(--white)}
.back-brand{position:absolute;top:262px;left:0;right:0;flex-direction:column;gap:4px}
.back-brand .brand__name{font-size:34px;line-height:1}
.tagline{font-size:5.5px;letter-spacing:.4px;text-transform:uppercase}
.contact{position:absolute;top:344px;left:0;right:0;text-align:center;font-size:12px;line-height:17px;letter-spacing:-.3px}
.social{position:absolute;left:44px;top:450px;font-size:11.5px;font-weight:600;line-height:23px}
.social li{list-style:none;display:flex;align-items:center;gap:8px}
.social__mark{width:14px;height:14px;background:#e6ecf8}
.cover-brand{position:absolute;left:129px;top:258px;transform:translate(-50%,-50%) rotate(-90deg);flex-direction:row;gap:14px;white-space:nowrap}
.cover-brand .brand__name{font-size:60px;line-height:1}
.cover-brand .brand__dot{width:56px;height:56px;transform:rotate(90deg)}
.cover-brand .tagline{font-size:8px;position:absolute;left:70px;top:-6px}
.heading{font-family:"Fira Sans Extra Condensed",sans-serif;font-weight:900;letter-spacing:-.5px}
.intro-box{position:absolute;left:32px;top:31px;width:194px;height:167px;background:var(--ink);padding:18px 22px}
.intro-box .heading{color:var(--blue);font-size:29px;line-height:24px;margin-bottom:8px}
.intro-box p{font-size:6.4px;line-height:8.2px;text-align:justify;margin-bottom:7px}
.section{position:absolute;left:32px;width:200px}
.section .heading{font-size:15.5px;line-height:14px;font-weight:800;padding-left:10px;margin-bottom:6px}
.bullets li{list-style:none;position:relative;padding-left:13px;font-size:6.3px;line-height:7.6px;margin-bottom:4px;text-align:justify}
.bullets li::before{content:"";position:absolute;left:0;top:1px;border-left:5px solid var(--white);border-top:3px solid transparent;border-bottom:3px solid transparent}
.section-rule{position:absolute;left:42px;width:182px;border-top:1px solid #1b2d66}
.features{padding:48px 42px 0 39px}
.features .heading{color:var(--blue);font-size:38px;line-height:31px;margin-bottom:19px;text-align:justify;text-align-last:justify}
.features .heading span{display:block}
.module-bar{background:var(--blue);color:var(--white);font-family:"Fira Sans Extra Condensed",sans-serif;font-weight:800;font-size:12px;padding:0 9px;line-height:15px;text-transform:uppercase;margin-bottom:3px}
.features ul{margin-bottom:9px}
.features li{list-style:none;font-size:6.2px;line-height:7.4px;margin-bottom:4px;text-align:justify}
.costs{padding:48px 52px 0 48px}
.costs .heading{color:var(--ink);font-size:38px;line-height:29px;margin-bottom:18px}
.label{background:var(--ink);font-size:6.8px;font-weight:700;text-transform:uppercase;padding:0 8px;line-height:9px;margin-bottom:0}
.price-box{background:var(--blue-light);font-size:7px;font-weight:600;line-height:8.6px;padding:6px 8px;margin-bottom:13px}
.price-box strong{display:block;text-transform:uppercase;font-size:7px}
.price-box--tall{height:56px;padding-top:9px}
.fine{font-size:6.4px;line-height:7px;text-transform:uppercase;letter-spacing:.3px;padding-bottom:3px;border-bottom:1.5px solid var(--ink);margin-top:34px}
.offer{font-size:6.6px;font-weight:700;line-height:8px;text-transform:uppercase;margin-top:4px}
.promo{background:var(--ink);color:var(--blue-light);font-family:"Fira Sans Extra Condensed",sans-serif;font-weight:900;font-size:21px;line-height:16.5px;text-transform:uppercase;padding:3px 3px 2px;margin-top:10px}
</style>
</head>
<body>

<section class="sheet sheet--outer">
  <div class="panel">
    <div class="app-screen" role="img" aria-label="Phone app screen showing a grid of app icons"></div>
  </div>

  <div class="panel panel--blue">
    <div class="brand back-brand">
      <span class="brand__dot"></span>
      <span class="brand__name">tulvora</span>
      <span class="tagline">Connecting teachers and parents</span>
    </div>
    <address class="contact" style="font-style:normal">
      Postal: Po Box<br>
      Email: info@tulvora.com.au<br>
      Ph:
    </address>
    <ul class="social">
      <li><span class="social__mark"></span>www.friendbook.com/tulvora</li>
      <li><span class="social__mark"></span>www.chirper.com/tulvoraau</li>
    </ul>
  </div>

  <div class="panel panel--blue">
    <div class="brand cover-brand">
      <span class="brand__dot"></span>
      <span class="brand__name">tulvora</span>
      <span class="tagline">Connecting teachers and parents</span>
    </div>
  </div>
</section>

<section class="sheet sheet--inner">
  <div class="panel panel--blue">
    <div class="intro-box">
      <h2 class="heading">What is Tulvora?</h2>
      <p>Tulvora is an interactive mobile app that connects schools, teachers and parents like never before, offering functionality like no other. Tulvora links the school community through Orbi phone and Verdan devices with real-time two-way communication.</p>
      <p>Tulvora was designed in Canberra, for Canberra schools (with KESTREL in mind) and will be supported out of Canberra.</p>
    </div>

    <div class="section" style="top:215px">
      <h3 class="heading">What problems does Tulvora solve for Parents?</h3>
      <ul class="bullets">
        <li>No more handwriting absence notes with instant two way absence notifications between school and parent</li>
        <li>No more lost permission slips in school bags with school to parent notifications and parent to school approvals</li>
        <li>No more rushed homework with homework and assignment reminders</li>
        <li>No lost lunch order money with in-app canteen ordering</li>
        <li>No more cheque writing or cash in envelopes with in-app payment capability</li>
      </ul>
    </div>
    <div class="section-rule" style="top:351px"></div>

    <div class="section" style="top:358px">
      <h3 class="heading">What does Tulvora do for Schools?</h3>
      <ul class="bullets">
        <li>Reduction of paper based activities through electronic roll marking and absence reporting</li>
        <li>Less time wasted counting lunchorder money with in-app canteen ordering</li>
        <li>Less administrative time banking cheques/cash with in-app payments for school expenses</li>
        <li>No last minute chasing of permissions through electronic notification and parent approvals</li>
        <li>No student data compromised as Tulvora doesn't interface with existing student management systems</li>
      </ul>
    </div>
  </div>

  <div class="panel panel--white features">
    <h2 class="heading"><span>Features of</span><span>Tulvora</span></h2>

    <div class="module-bar">Admin Module</div>
    <ul>
      <li>Dedicated web portal in a hosted cloud or on the school intranet in multiple languages</li>
      <li>Parents can pay school fees, excursions and other payments in-app</li>
      <li>School lunch orders can be ordered in-app</li>
      <li>Student awards and reports can be uploaded into the app for parents to view</li>
      <li>School newsletters can be uploaded into the app</li>
      <li>Principal's Corner for executive messages to parents and teachers</li>
      <li>Parents can provide feedback to the school in-app</li>
      <li>RSS feeds can be received in-app</li>
      <li>Mobile app supports multiple languages</li>
    </ul>

    <div class="module-bar">Notification Module</div>
    <ul>
      <li>Push notifications to parents for school events &amp; information</li>
      <li>Parents can approve their child's school event attendance in-app</li>
      <li>Homework and assignment notifications sent to parents</li>
    </ul>

    <div class="module-bar">Absence Module</div>
    <ul>
      <li>Teacher Roll marking on any OrbiOS and Verdan smart device</li>
      <li>Instant student absence notification to parent through push notification</li>
      <li>Ability for parent to instantly respond in-app to school to explain absence</li>
      <li>PDF documents automatically generated in-app for audit requirement</li>
    </ul>
  </div>

  <div class="panel panel--blue costs">
    <h2 class="heading">Tulvora Costs</h2>

    <p class="label">Purchase fee:</p>
    <div class="price-box" style="padding:3px 8px;margin-bottom:13px">Once off purchase fee $700</div>

    <p class="label">Annual licence fees:</p>
    <div class="price-box price-box--tall" style="margin-top:5px">
      <strong>Any one module</strong>
      &lt;500 students = $300<br>&lt;800 students = $600<br>&gt;800 students = $800
    </div>
    <div class="price-box price-box--tall">
      <strong>Any two modules</strong>
      &lt;500 students = $400<br>&lt;800 students = $700<br>&gt;800 students = $900
    </div>
    <div class="price-box price-box--tall">
      <strong>All three modules</strong>
      &lt;500 students = $500<br>&lt;800 students = $800<br>&gt;800 students = $1000
    </div>

    <p class="fine">All prices quoted are in AUD and are inclusive of 10% GST.</p>
    <p class="offer">Sign up for 3 years and receive 25% discount on licencing fees</p>
    <p class="promo">First 10 schools to sign up receive their first year free</p>
  </div>
</section>

</body>
</html>
```